Pebble Lane real estate investment company needs a poster design

We would like a poster design size 18 x 24.
Poster wording -
I WANT TO BUY YOUR ( finish with logo) logo uploaded
website- www.pebblelane-homes.example
phone # 555-217-8843 ( color red for the phone number)
we would like to see the poster on 2 different backgrounds
Yellow background
White background
horizontal

```html
<!DOCTYPE html>
<html lang="en">
<head>
<meta charset="utf-8">
<title>Pebble Lane Poster – Horizontal Versions</title>
<link href="https://fonts.googleapis.com/css2?family=Archivo+Black&family=Arimo:wght@700&display=swap" rel="stylesheet">
<style>
  :root {
    --page: #eeeeee;
    --brand-red: #d2232a;
    --ink: #0d0d0d;
    --paper: #ffffff;
    --sun-yellow: #f6c928;
    --frame-line: #d6d6d6;
    --stone-dark: #3b3b3b;
    --stone-light: #9a9a9a;
  }
  html, body {
    margin: 0;
    width: 1200px;
    height: 1200px;
    overflow: hidden;
    background: var(--page);
  }
  .poster {
    --backdrop: var(--paper);
    position: absolute;
    left: 220px;
    width: 760px;
    height: 570px;
    overflow: hidden;
    background: var(--backdrop);
    box-sizing: border-box;
  }
  .poster--yellow { top: 20px; --backdrop: var(--sun-yellow); }
  .poster--white { top: 610px; --backdrop: var(--paper); border: 1px solid var(--frame-line); }

  .text-column {
    position: absolute;
    left: 40px;
    top: 0;
    width: 300px;
    height: 100%;
    background: var(--paper);
  }
  .band {
    position: absolute;
    left: 40px;
    width: 300px;
    height: 34px;
    background: var(--brand-red);
  }
  .band--top { top: 0; }
  .band--bottom { bottom: 0; }

  .window-photo {
    position: absolute;
    left: 340px;
    top: 34px;
    width: 380px;
    height: 500px;
    background: linear-gradient(90deg, var(--stone-dark) 0%, #5c5c5c 45%, var(--stone-light) 100%);
  }
  .contact-veil {
    position: absolute;
    left: 340px;
    top: 330px;
    width: 380px;
    height: 204px;
    background: rgba(255, 255, 255, 0.72);
  }

  .headline {
    position: absolute;
    left: 66px;
    top: 54px;
    margin: 0;
    font-family: "Archivo Black", sans-serif;
    font-size: 60px;
    line-height: 54px;
    letter-spacing: -1px;
    color: var(--ink);
  }
  .brand-name {
    position: absolute;
    left: 0;
    width: 100%;
    top: 346px;
    text-align: center;
    font-family: "Archivo Black", sans-serif;
    font-size: 54px;
    line-height: 64px;
    letter-spacing: -1px;
    color: var(--ink);
  }
  .contact {
    position: absolute;
    left: 0;
    width: 100%;
    text-align: center;
    font-family: "Arimo", sans-serif;
    font-weight: 700;
  }
  .contact--web {
    top: 430px;
    font-size: 21px;
    line-height: 26px;
    color: var(--ink);
  }
  .contact--phone {
    top: 460px;
    font-size: 36px;
    line-height: 42px;
    letter-spacing: 2px;
    color: var(--brand-red);
  }
</style>
</head>
<body>
  <main class="poster poster--yellow">
    <div class="text-column"></div>
    <div class="band band--top"></div>
    <div class="band band--bottom"></div>
    <div class="window-photo" role="img" aria-label="Black and white photo of an old barred window in a crumbling brick wall"></div>
    <div class="contact-veil"></div>
    <h1 class="headline">I<br>WANT<br>TO<br>BUY<br>YOUR</h1>
    <div class="brand-name">Pebble Lane</div>
    <div class="contact contact--web">www.pebblelane-homes.example</div>
    <div class="contact contact--phone">555-217-8843</div>
  </main>

  <main class="poster poster--white">
    <div class="text-column"></div>
    <div class="band band--top"></div>
    <div class="band band--bottom"></div>
    <div class="window-photo" role="img" aria-label="Black and white photo of an old barred window in a crumbling brick wall"></div>
    <div class="contact-veil"></div>
    <h1 class="headline">I<br>WANT<br>TO<br>BUY<br>YOUR</h1>
    <div class="brand-name">Pebble Lane</div>
    <div class="contact contact--web">www.pebblelane-homes.example</div>
    <div class="contact contact--phone">555-217-8843</div>
  </main>
</body>
</html>
```